Varnel Group Limited Stationary

We are in need of business card and letterhead designs. We are looking for clean modern designs that complement the style and feel of our logo.

Industry/Entity Type

Business

```html
<!DOCTYPE html>
<html lang="en">
<head>
<meta charset="utf-8">
<title>Varnel Group Limited – Business Card</title>
<link rel="stylesheet" href="https://fonts.googleapis.com/css2?family=Questrial&family=Open+Sans:wght@700&display=swap">
<style>
  :root {
    --page: #d9dadc;
    --card-white: #f6f6f4;
    --brand-blue: #0f3d8c;
    --brand-blue-light: #1c4fa6;
    --charcoal: #3a3d42;
    --text-grey: #4a4a4a;
    --white: #ffffff;
  }
  * { box-sizing: border-box; margin: 0; padding: 0; }
  html, body { width: 1200px; height: 1000px; overflow: hidden; }
  body { background: var(--page); position: relative; font-family: "Questrial", sans-serif; }

  .card {
    position: absolute;
    width: 528px;
    height: 302px;
    border-radius: 14px;
    overflow: hidden;
    box-shadow: 0 2px 6px rgba(0,0,0,0.25);
  }

  /* Front */
  .card-front { left: 207px; top: 165px; background: var(--card-white); }
  .front-company {
    position: absolute; left: 36px; top: 56px;
    font-size: 25px; color: var(--brand-blue); letter-spacing: 0.5px;
  }
  .holder { position: absolute; right: 50px; top: 56px; text-align: right; }
  .holder-name {
    font-family: "Open Sans", sans-serif; font-weight: 700;
    font-size: 21px; color: var(--brand-blue); letter-spacing: 0.3px; line-height: 1.1;
  }
  .holder-title { font-size: 16px; color: var(--text-grey); margin-top: 2px; }
  .address {
    position: absolute; left: 35px; top: 143px;
    font-size: 13px; line-height: 18px; color: var(--text-grey);
  }
  .contacts { position: absolute; left: 35px; top: 189px; list-style: none; }
  .contacts li {
    display: flex; align-items: center; height: 17.7px;
    font-size: 13px; color: var(--text-grey);
  }
  .contacts svg { width: 13px; height: 13px; margin-right: 9px; flex: none; }
  .front-band {
    position: absolute; left: 0; right: 0; bottom: 0; height: 15px;
    background: var(--brand-blue);
  }
  .front-disc {
    position: absolute; left: 412px; top: 190px;
    width: 130px; height: 130px; border-radius: 50%;
    background: var(--charcoal); border: 7px solid var(--brand-blue);
  }

  /* Back */
  .card-back {
    left: 474px; top: 551px;
    background: linear-gradient(160deg, var(--brand-blue-light), var(--brand-blue));
  }
  .back-company {
    position: absolute; left: 29px; top: 128px;
    font-size: 29px; color: var(--white); letter-spacing: 0.6px;
  }
  .back-disc {
    position: absolute; left: 293px; top: 22px;
    width: 240px; height: 240px; border-radius: 50%;
    background: var(--charcoal);
  }
</style>
</head>
<body>

<section class="card card-front" aria-label="Business card front">
  <p class="front-company">Varnel Group</p>
  <div class="holder">
    <p class="holder-name">MARA ELLISON</p>
    <p class="holder-title">Managing Director</p>
  </div>
  <p class="address">Suite 4, 27B Calloway Street<br>Brindale QLD 4821</p>
  <ul class="contacts">
    <li>
      <svg viewBox="0 0 13 13" aria-hidden="true"><rect width="13" height="13" rx="2" fill="#0f3d8c"/><rect x="4" y="2.5" width="5" height="8" rx="1" fill="none" stroke="#fff" stroke-width="1.2"/></svg>
      955.210.7734
    </li>
    <li>
      <svg viewBox="0 0 13 13" aria-hidden="true"><rect width="13" height="13" rx="2" fill="#0f3d8c"/><rect x="4" y="2.5" width="5" height="2.5" fill="#fff"/><rect x="2.5" y="5.5" width="8" height="3.5" fill="#fff"/><rect x="4" y="8.5" width="5" height="2.5" fill="none" stroke="#fff" stroke-width="1"/></svg>
      966.318.2046
    </li>
    <li>
      <svg viewBox="0 0 13 13" aria-hidden="true"><rect width="13" height="13" rx="2" fill="#0f3d8c"/><rect x="2.5" y="3.5" width="8" height="6" fill="none" stroke="#fff" stroke-width="1.1"/><path d="M2.5 3.8 L6.5 7 L10.5 3.8" fill="none" stroke="#fff" stroke-width="1.1"/></svg>
      info@varnelgroup.com
    </li>
    <li>
      <svg viewBox="0 0 13 13" aria-hidden="true"><rect width="13" height="13" rx="2" fill="#0f3d8c"/><circle cx="6.5" cy="6.5" r="4" fill="none" stroke="#fff" stroke-width="1"/><ellipse cx="6.5" cy="6.5" rx="1.8" ry="4" fill="none" stroke="#fff" stroke-width="0.9"/><line x1="2.5" y1="6.5" x2="10.5" y2="6.5" stroke="#fff" stroke-width="0.9"/></svg>
      www.varnelgroup.com
    </li>
  </ul>
  <div class="front-band"></div>
  <div class="front-disc"></div>
</section>

<section class="card card-back" aria-label="Business card back">
  <p class="back-company">Varnel Group</p>
  <div class="back-disc"></div>
</section>

</body>
</html>
```